Morvit Letterhead/product brochures
Letterhead/Product brochures
Creative Brief
Health
Clean, Professional, Serious
Colors much match current logo, and must include watermark. Pleas use the following information on the letterhead and sales sheet. Some of the examples of sales sheet are uploaded. Gerald Trumbo, MBA President/CEO Morvit Development 2863 Birchmoor Plaza #418 Walnut Creek, CA 94597 Tel: 925-614-5839 Fax: 925-552-7160 Cell: 925-246-9071 Email: gtrumbo@morvitdevelopment.example Single 8-1/2 x 11, both sides, non folding brochures The products are ingredients to the nutritional supplement industry. Examples attached.

```html
<!DOCTYPE html>
<html lang="en">
<head>
<meta charset="utf-8">
<title>Morvit Development – Stationery and Brochure Set</title>
<link rel="stylesheet" href="https://fonts.googleapis.com/css2?family=Arimo:ital,wght@0,400;0,700;1,700&display=swap">
<style>
:root{
  --navy:#1b4f8c;
  --sky:#3a9be0;
  --ink:#333a44;
  --muted:#6b7480;
  --line:#c9ced6;
  --paper:#ffffff;
  --stage:#ffffff;
  --band:#5b636e;
  --fog:#dfe3e8;
}
*{box-sizing:border-box;margin:0;padding:0}
html,body{width:1200px;height:732px;overflow:hidden;background:var(--stage)}
body{position:relative;font-family:"Arimo",Arial,sans-serif;color:var(--ink)}
.sheet{position:absolute;background:var(--paper);box-shadow:0 0 0 1px var(--line);overflow:hidden}
.swoosh{position:absolute;left:0;bottom:0;width:100%;display:block}
.brand{display:flex;align-items:center;gap:4px;color:var(--navy);font-weight:700;letter-spacing:.5px}
.brand .mark{background:var(--sky);display:block}
.photo{position:absolute;display:block}
.tiny{font-size:4.6px;line-height:1.35;color:var(--muted)}
.label{position:absolute;font-size:5px;color:var(--muted)}

/* tri-fold brochure */
.trifold{left:6px;width:462px}
.trifold.outside{top:12px;height:288px}
.trifold.inside{top:384px;height:336px}
.panel{position:absolute;top:0;width:154px;height:100%;border-right:1px solid var(--fog)}
.panel:nth-child(1){left:0}.panel:nth-child(2){left:154px}.panel:nth-child(3){left:308px;border-right:0}
.panel-head{background:var(--navy);color:#fff;font-size:6.5px;font-weight:700;padding:4px 8px;margin:8px 0 6px}
.panel .copy{padding:0 8px}
.panel .copy p{margin-bottom:4px}
.ticks{list-style:none;padding:2px 8px}
.ticks li{display:flex;align-items:center;gap:3px;font-size:4.6px;color:var(--muted);margin-bottom:2.5px}
.ticks svg{width:5px;height:5px}
.item-title{font-size:5px;font-weight:700;color:var(--navy)}
.headline{color:var(--navy);font-weight:700;font-style:italic;text-align:right;line-height:1.1}
.address{position:absolute;left:0;width:100%;text-align:center}
.web{position:absolute;left:0;bottom:6px;width:100%;text-align:center;font-size:4.6px;color:#fff}

/* letterhead */
.letterhead{left:492px;top:12px;width:240px;height:310px}
.letterhead .brand{position:absolute;left:14px;top:16px;font-size:13px}
.letterhead .brand .mark{width:10px;height:10px}
.foot-line{position:absolute;left:0;bottom:4px;width:100%;text-align:center;font-size:3.8px;color:#fff}

/* sales sheet */
.salesheet{left:842px;top:12px;width:350px;height:318px}
.salesheet .brand{position:absolute;left:12px;top:12px;font-size:14px}
.salesheet .brand .mark{width:11px;height:11px}
.salesheet .headline{position:absolute;right:12px;top:12px;font-size:12px}
.salesheet .intro{position:absolute;left:12px;top:52px;width:326px}
.salesheet .intro h2{font-size:6.5px;color:var(--navy);margin-bottom:3px}
.salesheet .list{position:absolute;left:12px;top:92px;width:178px}
.salesheet .list h3{font-size:5px;color:var(--navy);margin-bottom:3px}
.salesheet .list .entry{margin-bottom:4px}
.round{border-radius:50%}
.signoff{position:absolute;left:12px;bottom:30px}
.signoff .name{font-size:6px;font-weight:700;color:var(--navy)}
.contact{position:absolute;right:12px;bottom:6px;font-size:3.8px;color:#fff;text-align:right}

/* envelope */
.envelope{left:492px;top:420px;width:240px;height:180px}
.envelope .brand{position:absolute;left:14px;top:14px;font-size:12px}
.envelope .brand .mark{width:9px;height:9px}
.envelope .return{position:absolute;left:14px;top:34px}
</style>
</head>
<body>

<svg width="0" height="0" style="position:absolute" aria-hidden="true">
  <defs>
    <symbol id="swoosh" viewBox="0 0 300 60" preserveAspectRatio="none">
      <path d="M0 60 L0 38 C100 20 200 8 300 0 L300 60Z" fill="#dfe3e8"/>
      <path d="M0 52 C110 24 210 12 300 4 L300 10 C210 19 110 31 12 56Z" fill="#3a9be0"/>
      <path d="M0 60 C120 32 220 22 300 14 L300 32 C220 37 130 45 70 60Z" fill="#1b4f8c"/>
      <path d="M70 60 C140 46 230 38 300 34 L300 60Z" fill="#5b636e"/>
    </symbol>
    <symbol id="tick" viewBox="0 0 10 10"><rect width="10" height="10" rx="2" fill="#3a9be0"/><path d="M2.5 5.2 L4.3 7 L7.6 3.2" stroke="#fff" stroke-width="1.4" fill="none"/></symbol>
  </defs>
</svg>

<!-- Tri-fold, outside -->
<span class="label" style="left:50px;top:3px">Inside Panels</span>
<span class="label" style="left:228px;top:3px">Back</span>
<span class="label" style="left:382px;top:3px">Cover</span>
<section class="sheet trifold outside">
  <div class="panel">
    <div class="panel-head">WHY MORVIT</div>
    <div class="copy tiny">
      <p>We source and supply premium nutritional ingredients to supplement makers. Our team blends science with care to deliver pure, tested and traceable materials for every formula.</p>
      <p>Every batch is checked in our lab before it ships, so partners can trust quality from start to finish.</p>
    </div>
    <div class="photo" role="img" aria-label="Woman in a white coat working in a laboratory" style="left:0;top:176px;width:154px;height:112px;background:linear-gradient(160deg,#e9eef3,#c7d2dd 60%,#9aa9b7)"></div>
  </div>
  <div class="panel">
    <div class="address tiny" style="top:128px">Morvit Development<br>2863 Birchmoor Plaza #418<br>Walnut Creek, CA 94597</div>
    <div class="brand" style="position:absolute;left:38px;top:156px;font-size:12px"><span class="mark" style="width:9px;height:9px"></span>MORVIT</div>
    <svg class="swoosh" height="70"><use href="#swoosh"/></svg>
    <div class="web">www.morvitdevelopment.example</div>
  </div>
  <div class="panel">
    <div class="headline" style="position:absolute;right:8px;top:10px;font-size:11px">Mastering Wellness<br>for Life</div>
    <div class="photo" role="img" aria-label="Test tubes with coloured liquids and hands holding a seedling" style="left:0;top:42px;width:154px;height:132px;background:linear-gradient(135deg,#3f6fa8,#6aa5d8 40%,#3c6a2e 75%,#2a3a24)"></div>
    <div class="brand" style="position:absolute;left:34px;top:190px;font-size:12px"><span class="mark" style="width:9px;height:9px"></span>MORVIT</div>
    <svg class="swoosh" height="70"><use href="#swoosh"/></svg>
  </div>
</section>

<!-- Letterhead -->
<section class="sheet letterhead">
  <div class="brand"><span class="mark"></span>MORVIT</div>
  <svg class="swoosh" height="80"><use href="#swoosh"/></svg>
  <div class="foot-line">2863 Birchmoor Plaza #418, Walnut Creek, CA 94597 &nbsp; Tel: 925-614-5839 &nbsp; Fax: 925-552-7160 &nbsp; gtrumbo@morvitdevelopment.example</div>
</section>

<!-- Sales sheet -->
<section class="sheet salesheet">
  <div class="brand"><span class="mark"></span>MORVIT</div>
  <div class="headline">Mastering Wellness<br>for Life</div>
  <div class="intro">
    <h2>Lorem is the notion of design.</h2>
    <p class="tiny">Morvit Development supplies clean, reliable ingredients to the nutritional supplement industry. We work closely with brands to match each need with proven materials, clear documentation and steady delivery schedules.</p>
  </div>
  <div class="list tiny">
    <h3>INGREDIENTS WE PROVIDE</h3>
    <div class="entry"><div class="item-title">Botanical Extracts</div>Standardized plant extracts for capsules and powders.</div>
    <div class="entry"><div class="item-title">Amino Acids</div>Pure grade amino acids for sports blends.</div>
    <div class="entry"><div class="item-title">Vitamins &amp; Minerals</div>Custom premixes built to your label claims.</div>
    <div class="entry"><div class="item-title">Probiotics</div>Stable cultures tested for count and purity.</div>
  </div>
  <div class="photo" role="img" aria-label="Laboratory glassware" style="left:200px;top:92px;width:66px;height:46px;background:linear-gradient(135deg,#8fb6db,#3f6fa8)"></div>
  <div class="photo" role="img" aria-label="Family outdoors" style="left:272px;top:92px;width:66px;height:46px;background:linear-gradient(135deg,#b9d08a,#6e8f45)"></div>
  <div class="photo" role="img" aria-label="Herbs and capsules" style="left:200px;top:144px;width:138px;height:46px;background:linear-gradient(135deg,#d7e3c0,#8aa864)"></div>
  <div class="photo round" role="img" aria-label="Fresh fruit" style="left:60px;top:200px;width:38px;height:38px;background:radial-gradient(#d9823a,#8a3e1c)"></div>
  <div class="photo round" role="img" aria-label="Green leaves" style="left:110px;top:200px;width:38px;height:38px;background:radial-gradient(#9cc46a,#3f6a2a)"></div>
  <div class="photo round" role="img" aria-label="Supplement tablets" style="left:160px;top:200px;width:38px;height:38px;background:radial-gradient(#f0f0ea,#a9aaa0)"></div>
  <div class="photo round" role="img" aria-label="Seedling in soil" style="left:210px;top:200px;width:38px;height:38px;background:radial-gradient(#7fa052,#4a3a26)"></div>
  <div class="signoff"><div class="name">Gerald Trumbo, MBA</div><div class="tiny">President/CEO</div></div>
  <svg class="swoosh" height="60"><use href="#swoosh"/></svg>
  <div class="contact">Morvit Development<br>Tel: 925-614-5839 &nbsp; Fax: 925-552-7160 &nbsp; Cell: 925-246-9071 &nbsp; gtrumbo@morvitdevelopment.example</div>
</section>

<!-- Tri-fold, inside -->
<section class="sheet trifold inside">
  <div class="panel">
    <div class="panel-head">ABOUT US</div>
    <div class="copy tiny">
      <p>Morvit Development was founded to give supplement makers a partner they can rely on. We bring years of sourcing experience and a strong network of growers and labs.</p>
      <p>Our mission is simple: clean ingredients, honest data and fast service.</p>
    </div>
    <div class="photo" role="img" aria-label="Doctor in a white coat" style="left:0;top:222px;width:154px;height:114px;background:linear-gradient(160deg,#eef2f5,#c3ced8)"></div>
  </div>
  <div class="panel">
    <div class="panel-head">SERVICES</div>
    <div class="copy tiny"><p>We help you plan, source and test each ingredient for your next product.</p></div>
    <ul class="ticks">
      <li><svg><use href="#tick"/></svg>Custom sourcing</li>
      <li><svg><use href="#tick"/></svg>Lab testing</li>
      <li><svg><use href="#tick"/></svg>Formula support</li>
      <li><svg><use href="#tick"/></svg>Private label</li>
      <li><svg><use href="#tick"/></svg>Bulk supply</li>
      <li><svg><use href="#tick"/></svg>Fast shipping</li>
    </ul>
    <div class="photo" role="img" aria-label="Green plants growing" style="left:0;top:222px;width:154px;height:114px;background:linear-gradient(160deg,#9fc36b,#3f6a2a)"></div>
  </div>
  <div class="panel">
    <div class="panel-head">PRODUCTS</div>
    <div class="copy tiny">
      <p><span class="item-title">Plant Extracts</span><br>Sourced from trusted growers worldwide.</p>
      <p><span class="item-title">Amino Acids</span><br>High purity for sports nutrition.</p>
      <p><span class="item-title">Specialty Blends</span><br>Made to match your formula.</p>
    </div>
    <div class="photo" role="img" aria-label="Hands holding soil with a sprout" style="left:0;top:222px;width:154px;height:114px;background:linear-gradient(160deg,#6b8d45,#5a4530)"></div>
  </div>
  <svg style="position:absolute;left:0;top:196px;width:462px;height:26px" viewBox="0 0 300 26" preserveAspectRatio="none" aria-hidden="true">
    <path d="M0 26 C100 10 200 4 300 0 L300 26Z" fill="#1b4f8c"/>
    <path d="M0 22 C100 6 200 2 300 0 L300 4 C200 7 100 12 0 26Z" fill="#3a9be0"/>
  </svg>
</section>

<!-- Envelope -->
<section class="sheet envelope">
  <div class="brand"><span class="mark"></span>MORVIT</div>
  <div class="return tiny">Morvit Development<br>2863 Birchmoor Plaza #418<br>Walnut Creek, CA 94597</div>
  <svg class="swoosh" height="56"><use href="#swoosh"/></svg>
</section>

</body>
</html>
```